Private Maths Tuition Flyer based in London

I am opening up a new Maths tuition centre in North West London. The flyer will be delivered to over 8,000 homes within the immediate vicinity. The design should be suitable to be printed on an A5 sheet and read in a portrait orientation.

The flyer should include the following:

The headline statement should be "Private Maths Tuition"

Secondary headline statement is the following "GCSE, A-Levels, 11 Plus exams"

Some of service offerings/selling points are:

- Free first session
- Monthly Feedback reports
- Free support outside of sessions
- Clear Target grades
- Personalised Lesson plans
- Tangible Results

Another statement that should be featured is "Book your free session by visiting www.lernova.co.uk" or something similar to that.

"Contact Details:
020 4719 8263
enquiries@lernova.co.uk"

"Address:
Kelbridge Business and Innovation Centre
Ashvale Court
Wrenfield Road
HA4 9QD"

Attached you'll see a logo which should be included and also a map of where we are. I am open to new images for the map if you guys have any, rather than a screen shot from google maps but it should be clear to see.

I would like the content above to be displayed in a clear and concise manner that is easy to read. You have creative license on where this information should be displayed and where the images should be but on the whole it should look aesthetically pleasing on the eye.

Target Market(s)

Students, Parents. Parents who want maths tutors.

Industry/Entity Type

Tutoring

Font styles to use
Sans Serif

Requirements
Must have
• *logo*
• Private Maths Tuition
• GCSE, A-Levels, 11 Plus exams
• - Free first session
• - Monthly Feedback reports
• - Free support outside of sessions
• - Clear Target grades
• - Personalised Lesson plans
• - Tangible Results
• Book your free session by visiting www.lernova.co.uk" or something similar to that.
• Contact Details:
• 020 4719 8263
• enquiries@lernova.co.uk
• Address (*with map*):
• Kelbridge Business and Innovation Centre
• Ashvale Court
• Wrenfield Road
• HA4 9QD
Nice to have
• similar colour scheme as the logo. creative background design.

```html
<!DOCTYPE html>
<html lang="en">
<head>
<meta charset="utf-8">
<title>Private Maths Tuition – Lernova</title>
<link href="https://fonts.googleapis.com/css2?family=Open+Sans:wght@400;600;700;800&display=swap" rel="stylesheet">
<style>
  :root{
    --orange:#f26b1d;
    --orange-dark:#d9520c;
    --green:#7cbf2c;
    --green-dark:#4f9a1e;
    --blue:#1d6fb8;
    --charcoal:#3a3a3c;
    --charcoal-dark:#262628;
    --ink:#333;
    --white:#fff;
  }
  *{box-sizing:border-box;margin:0;padding:0}
  html,body{width:826px;height:1200px;overflow:hidden}
  body{font-family:"Open Sans",Arial,sans-serif;background:var(--white);color:var(--ink)}
  .flyer{position:relative;width:826px;height:1200px;overflow:hidden;background:var(--white)}
  .abs{position:absolute}

  .hero-photo{left:360px;top:0;width:466px;height:560px;background:linear-gradient(135deg,#c9b08a 0%,#e8d7bd 40%,#8fb0c9 75%,#5b7fa3 100%)}
  .headline{left:0;top:0;width:420px;height:250px}
  .headline-text{left:48px;top:52px;color:var(--white)}
  .headline-text .kicker{font-size:36px;font-weight:800;letter-spacing:.5px;line-height:1}
  .headline-text .main{font-size:86px;font-weight:800;line-height:1;margin-top:4px}

  .brand-band{left:0;top:250px;width:826px;height:200px}
  .brand{left:50px;top:312px;display:flex;align-items:center;gap:12px}
  .brand-mark{width:20px;height:20px;border-radius:50%;background:var(--green)}
  .brand-name{font-size:54px;font-weight:700;color:var(--white);line-height:1}

  .thumb{border:5px solid var(--white);border-radius:12px;box-shadow:0 3px 8px rgba(0,0,0,.3)}
  .thumb-laptop{left:345px;top:240px;width:130px;height:90px;background:linear-gradient(135deg,#7a8a99,#d8dde2)}
  .thumb-group{left:345px;top:342px;width:130px;height:90px;background:linear-gradient(135deg,#b79a7a,#6f8fae)}

  .cta-band{left:0;top:450px;width:500px;height:180px}
  .cta-text{left:46px;top:485px;color:var(--white);font-weight:700}
  .cta-text .line{font-size:36px;line-height:1.1}
  .cta-text .url{font-size:30px;margin-top:6px}

  .contact{left:0;top:640px;width:430px;height:110px;background:var(--blue);color:var(--white);padding:16px 0 0 46px}
  .contact .label{font-size:26px;font-weight:700}
  .contact .phone{font-size:38px;font-weight:600;line-height:1.2}

  .map{left:0;top:772px;width:430px;height:220px;background:linear-gradient(135deg,#e9ece4,#dfe5ee 60%,#e8e2d6)}

  .courses{right:48px;top:570px;text-align:right}
  .courses .levels{font-size:42px;font-weight:400;color:var(--ink);line-height:1.1}
  .courses .plus{font-size:50px;font-weight:400;color:var(--orange);line-height:1.1}
  .benefits{list-style:none;margin-top:14px}
  .benefits li{font-size:19px;line-height:28px;color:var(--ink);display:flex;justify-content:flex-end;align-items:center;gap:12px}
  .benefits li::after{content:"";width:11px;height:11px;background:var(--orange)}

  .email{left:470px;top:895px;width:200px}
  .email .label{font-size:32px;font-weight:700;color:var(--orange);line-height:1.1}
  .email .address{font-size:14px;color:var(--orange-dark);margin-top:4px}
  .email-photo{left:680px;top:878px;width:130px;height:120px;background:linear-gradient(160deg,#dbe7c9,#7cbf2c 90%);border-radius:8px}

  .footer{left:0;top:990px;width:826px;height:210px}
  .footer-address{right:48px;top:1050px;text-align:right;color:var(--white);font-size:20px;font-weight:600;line-height:1.45}
</style>
</head>
<body>
<div class="flyer">

  <div class="abs hero-photo" role="img" aria-label="Photo of smiling students studying together at a table in a library"></div>

  <svg class="abs headline" viewBox="0 0 420 250" aria-hidden="true">
    <path d="M0 0H420V150Q400 230 320 250H0Z" fill="var(--orange)"/>
  </svg>
  <div class="abs headline-text">
    <div class="kicker">PRIVATE MATHS</div>
    <div class="main">TUITION</div>
  </div>

  <svg class="abs brand-band" viewBox="0 0 826 200" aria-hidden="true">
    <path d="M0 0H330Q400 0 430 60Q470 150 560 170Q650 190 826 160V200H0Z" fill="var(--charcoal)"/>
    <path d="M0 0H330Q400 0 430 60Q470 150 560 170Q650 190 826 160V185Q650 215 560 195Q450 175 415 80Q390 20 330 20H0Z" fill="var(--charcoal-dark)"/>
  </svg>
  <div class="abs brand">
    <span class="brand-mark"></span>
    <span class="brand-name">Lernova</span>
  </div>

  <div class="abs thumb thumb-laptop" role="img" aria-label="Photo of a laptop on a desk"></div>
  <div class="abs thumb thumb-group" role="img" aria-label="Photo of a group of students"></div>

  <svg class="abs cta-band" viewBox="0 0 500 180" aria-hidden="true">
    <path d="M0 0H420Q480 0 490 60Q500 150 430 180H0Z" fill="var(--green-dark)"/>
    <path d="M0 0H400Q460 0 470 55Q478 140 410 170H0Z" fill="var(--green)"/>
  </svg>
  <div class="abs cta-text">
    <div class="line">Book your free</div>
    <div class="line">session by visiting</div>
    <div class="url">www.lernova.co.uk</div>
  </div>

  <div class="abs contact">
    <div class="label">Contact Details:</div>
    <div class="phone">020 4719 8263</div>
  </div>

  <div class="abs map" role="img" aria-label="Street map showing the location of the tuition centre"></div>

  <div class="abs courses">
    <div class="levels">GCSE, A-Levels</div>
    <div class="plus">11 Plus exams</div>
    <ul class="benefits">
      <li>Free first session</li>
      <li>Monthly Feedback reports</li>
      <li>Free support outside of sessions</li>
      <li>Clear Target grades</li>
      <li>Personalised Lesson plans</li>
      <li>Tangible Results</li>
    </ul>
  </div>

  <div class="abs email">
    <div class="label">Email us at</div>
    <div class="address">enquiries@lernova.co.uk</div>
  </div>
  <div class="abs email-photo" role="img" aria-label="Photo of a student working on a laptop"></div>

  <svg class="abs footer" viewBox="0 0 826 210" aria-hidden="true">
    <path d="M0 120Q300 60 560 40Q700 30 826 20V210H0Z" fill="var(--charcoal)"/>
    <path d="M380 45Q600 30 826 20V150H300Q330 60 380 45Z" fill="var(--orange)"/>
    <path d="M0 150Q200 120 300 150H826V165H0Z" fill="var(--green)"/>
  </svg>
  <div class="abs footer-address">
    Kelbridge Business and Innovation Centre<br>
    Ashvale Court, Wrenfield Road, HA4 9QD
  </div>

</div>
</body>
</html>
```